Website Design - Photo Shop Design - Functional Cash Register Layout for POS System

Design a webpage for Point of Sale site. A cash register page.

Page must have a good look. I have attached a file of a possible layout example - but need a much nicer design. I have also attached the site logo. which i will upload without background tomorrow hopefully.

Looking for a nice Fresh look , not dark and dingy.

Target Market(s)

Business

Industry/Entity Type

Business Software

Number of Pages Required

1 page

Colors
f59195
f04a50
ec1f27
fbd4d5
ffffff
f8f3f8
fdf0f6
feeeee
ecf5f6

Requirements
Must have
• Cash register layout for POS software site. Nice layout ,
Nice to have
• Try putting he register part on the left side as well as the right - invert the designs have them different to the layout example shown too.
Should not have
• Not to dark

```html
<!DOCTYPE html>
<html lang="en">
<head>
<meta charset="utf-8">
<title>TillNimbus – Register</title>
<link rel="stylesheet" href="https://fonts.googleapis.com/css2?family=Maven+Pro:wght@400;500;700&display=swap">
<style>
:root{
  --header-dark:#111;
  --header-mid:#3a3a3a;
  --brand-red:#f04a50;
  --brand-pink:#f59195;
  --delete-red:#e8141c;
  --receipt-bg:#f6f1f7;
  --pale-teal:#ecf2f4;
  --pale-teal-line:#d5dfe2;
  --panel-line:#dcdfe1;
  --category-dark:#464b4f;
  --text-dark:#3d4246;
  --text-grey:#8c8c8c;
  --text-soft:#9aa1a5;
  --pay-green:#77cf7e;
  --white:#fff;
}
*{box-sizing:border-box;margin:0;padding:0}
html,body{width:1200px;height:1000px;overflow:hidden;background:var(--white);font-family:"Maven Pro",sans-serif}
.register{position:relative;width:1200px;height:1000px}
.topbar{position:absolute;left:0;top:0;width:1200px;height:74px;background:linear-gradient(90deg,var(--header-dark) 0%,#1b1b1b 60%,var(--header-mid) 100%);display:flex;align-items:center;justify-content:center}
.brand{display:flex;align-items:center;gap:10px;color:var(--white);font-size:30px;font-weight:500;letter-spacing:.5px}
.brand-dot{width:26px;height:26px;border-radius:50%;background:var(--brand-red)}

.catalog{position:absolute;left:60px;top:106px;width:720px;height:839px;border:1px solid var(--panel-line);background:var(--white)}
.category-head{height:47px;background:var(--category-dark);color:var(--white);font-size:24px;padding-left:28px;line-height:47px;letter-spacing:.5px}
.product{position:absolute;left:29px;width:660px;height:45px;border:1px solid var(--panel-line);font-size:24px;color:var(--text-grey);padding-left:29px;line-height:43px}
.product.is-selected{background:var(--brand-pink);border-color:var(--brand-pink);color:var(--white);font-weight:700}
.category{position:absolute;left:-1px;width:720px;height:45px;background:var(--pale-teal);border:1px solid var(--pale-teal-line);color:var(--text-dark);font-size:25px;padding-left:28px;line-height:43px;letter-spacing:.3px}

.cancel{position:absolute;left:840px;top:75px;width:330px;height:75px;background:var(--brand-red);color:var(--white);display:flex;align-items:center;justify-content:center;gap:10px;font-size:36px;letter-spacing:.5px}
.receipt{position:absolute;left:840px;top:150px;width:330px;height:595px;background:var(--receipt-bg);filter:drop-shadow(0 2px 3px rgba(0,0,0,.18));
  clip-path:polygon(0 0,100% 0,100% 98%,97% 100%,94% 98%,91% 100%,88% 98%,85% 100%,82% 98%,79% 100%,76% 98%,73% 100%,70% 98%,67% 100%,64% 98%,61% 100%,58% 98%,55% 100%,52% 98%,49% 100%,46% 98%,43% 100%,40% 98%,37% 100%,34% 98%,31% 100%,28% 98%,25% 100%,22% 98%,19% 100%,16% 98%,13% 100%,10% 98%,7% 100%,4% 98%,0 100%)}
.customer{position:absolute;left:39px;top:17px;display:flex;gap:14px;align-items:flex-start}
.customer-label{color:var(--text-grey);font-size:36px;line-height:40px}
.customer-label strong{display:block;font-weight:700;font-size:34px;line-height:44px}
.line-items{position:absolute;left:20px;top:113px;width:293px;height:312px;background:var(--white)}
.line{position:absolute;left:15px;width:261px;height:44px;border-bottom:2px solid #a6a6a6;font-size:16px;color:var(--text-grey);display:flex;align-items:center;justify-content:space-between}
.line-main{display:flex;gap:14px}
.line-actions{display:flex;gap:2px;align-self:flex-end;margin-bottom:3px}
.btn-edit,.btn-delete{width:54px;height:35px;display:flex;align-items:center;justify-content:center}
.btn-edit{background:#e6f0f2;border:1px solid #cfdde0}
.btn-delete{background:var(--delete-red)}
.totals{position:absolute;left:19px;top:462px;width:292px;font-size:22px;color:var(--text-grey)}
.totals div{display:flex;justify-content:space-between;height:36px}
.totals dt{font-weight:700}
.totals dd{font-size:24px}

.option{position:absolute;top:795px;width:163px;height:73px;background:var(--pale-teal);border:1px solid var(--pale-teal-line);color:var(--text-soft);font-size:26px;display:flex;align-items:center;justify-content:center;letter-spacing:.5px}
.pay{position:absolute;top:870px;width:163px;height:74px;background:var(--pay-green);display:flex;align-items:center;justify-content:center}
</style>
</head>
<body>
<main class="register">
  <header class="topbar"><div class="brand"><span class="brand-dot"></span>TillNimbus</div></header>

  <section class="catalog">
    <div class="category-head">PHONES</div>
    <div class="product" style="top:50px">7 Inch, 64GB</div>
    <div class="product" style="top:107px">7 Inch, 128GB</div>
    <div class="product is-selected" style="top:165px">6.5 Inch, 64GB</div>
    <div class="product" style="top:224px">6.5 Inch, 128GB</div>
    <div class="category" style="top:700px">LAPTOPS</div>
    <div class="category" style="top:747px">DESKTOPS</div>
    <div class="category" style="top:793px">ACCESSORIES</div>
  </section>

  <div class="cancel">
    <svg width="54" height="54" viewBox="0 0 54 54"><circle cx="27" cy="27" r="23" fill="none" stroke="#fff" stroke-width="6"/><line x1="13" y1="41" x2="41" y2="13" stroke="#fff" stroke-width="6"/></svg>
    CANCEL
  </div>

  <section class="receipt">
    <div class="customer">
      <svg width="72" height="72" viewBox="0 0 72 72"><circle cx="36" cy="36" r="33" fill="none" stroke="#8c8c8c" stroke-width="5"/><clipPath id="avatar-clip"><circle cx="36" cy="36" r="31"/></clipPath><g clip-path="url(#avatar-clip)" fill="#8c8c8c"><ellipse cx="36" cy="29" rx="11" ry="14"/><path d="M12 66c0-14 10-21 24-21s24 7 24 21z"/></g></svg>
      <div class="customer-label">Customer<strong>Name</strong></div>
    </div>
    <div class="line-items">
      <div class="line" style="top:0"><span>Item</span><span>$00.00</span></div>
      <div class="line" style="top:45px"><span>Item, descriptor, des...</span><span>$00.00</span></div>
      <div class="line" style="top:91px">
        <span class="line-main"><span>Item</span><span>$00.00</span></span>
        <span class="line-actions">
          <span class="btn-edit"><svg width="26" height="26" viewBox="0 0 26 26"><path d="M4 22l2-6L18 4l4 4-12 12z" fill="none" stroke="#8c8c8c" stroke-width="1.6"/><line x1="15" y1="7" x2="19" y2="11" stroke="#8c8c8c" stroke-width="1.6"/></svg></span>
          <span class="btn-delete"><svg width="24" height="26" viewBox="0 0 24 26"><rect x="2" y="3" width="20" height="2" fill="#fff"/><rect x="9" y="0" width="6" height="3" fill="#fff"/><rect x="4" y="7" width="16" height="18" fill="none" stroke="#fff" stroke-width="2"/><g stroke="#fff" stroke-width="1.6"><line x1="8" y1="10" x2="8" y2="22"/><line x1="12" y1="10" x2="12" y2="22"/><line x1="16" y1="10" x2="16" y2="22"/></g></svg></span>
        </span>
      </div>
    </div>
    <dl class="totals">
      <div><dt>Subtotal</dt><dd>$00.00</dd></div>
      <div><dt>Tax</dt><dd>$00.00</dd></div>
      <div><dt>Total</dt><dd>$00.00</dd></div>
    </dl>
  </section>

  <div class="option" style="left:842px">OPTION</div>
  <div class="option" style="left:1007px">OPTION</div>
  <div class="pay" style="left:842px" aria-label="Card payment">
    <svg width="82" height="56" viewBox="0 0 82 56"><rect x="3" y="3" width="76" height="50" rx="5" fill="none" stroke="#fff" stroke-width="5"/><rect x="14" y="14" width="10" height="12" fill="#fff"/><circle cx="48" cy="20" r="7" fill="#fff"/><circle cx="58" cy="20" r="7" fill="#fff"/><g fill="#fff"><rect x="14" y="34" width="10" height="4"/><rect x="28" y="34" width="10" height="4"/><rect x="42" y="34" width="10" height="4"/><rect x="14" y="42" width="30" height="3"/></g></svg>
  </div>
  <div class="pay" style="left:1007px" aria-label="Cash payment">
    <svg width="80" height="54" viewBox="0 0 80 54"><g transform="rotate(-14 40 27)" fill="none" stroke="#fff" stroke-width="4"><rect x="12" y="10" width="60" height="30"/><path d="M6 20v28h62"/></g><circle cx="43" cy="22" r="7" fill="#fff"/><text x="43" y="26" font-size="10" text-anchor="middle" fill="#77cf7e" font-family="Maven Pro, sans-serif" font-weight="700">$</text></svg>
  </div>
</main>
</body>
</html>
```